Bottle label design for a mulberry brandy

Please create a label design for a mulberry brandy. The registered brand name is "Kolvat"
The brandy will be produced in Armenia from 100% mulberry.
Color of the product: transparent.
The product will be sold worldwide. The price will be between 30 and 50 USD. So the product will be in premium category.
Therefore we need a solid design, appropriate to the product price category. The design, however, needs to be modern and optimistic.
You can have mulberries on the label or not have, it is up to you.
We have chosen for the product some bottle types, the links to the available bottles you can find in the attachment. Ideally you show a picture of your label on the bottle you selected.

Target Market(s)

worldwide

```html
<!DOCTYPE html>
<html lang="en">
<head>
<meta charset="utf-8">
<title>Kolvat Mulberry Brandy Label</title>
<link href="https://fonts.googleapis.com/css2?family=Cinzel:wght@400&family=Great+Vibes&family=Josefin+Sans:wght@400;600&display=swap" rel="stylesheet">
<style>
  :root {
    --bg: #ffffff;
    --gold-bright: #ecc100;
    --gold: #c9a212;
    --gold-deep: #b8930c;
    --leaf: #6faa2e;
    --leaf-dark: #3f7a1c;
    --berry: #4a2a4a;
  }
  * { margin: 0; padding: 0; box-sizing: border-box; }
  html, body {
    width: 1029px; height: 1200px; overflow: hidden; background: var(--bg);
  }
  .label {
    position: relative; width: 1029px; height: 1200px;
    display: flex; flex-direction: column; align-items: center;
  }
  .illustration {
    position: absolute; top: 150px; left: 50%; transform: translateX(-50%);
    width: 440px; height: 470px;
  }
  .brand {
    position: absolute; top: 370px; left: 0; width: 100%; text-align: center;
    font-family: "Cinzel", serif; font-weight: 400; font-size: 150px;
    line-height: 1; color: var(--gold-bright); letter-spacing: -2px;
  }
  .product {
    position: absolute; top: 640px; left: 0; width: 100%; text-align: center;
  }
  .product-fruit {
    font-family: "Great Vibes", cursive; font-size: 130px; line-height: 1;
    color: var(--gold);
  }
  .product-type {
    margin-top: -4px;
    font-family: "Josefin Sans", sans-serif; font-weight: 600; font-size: 32px;
    letter-spacing: 9px; color: var(--gold);
  }
  .age {
    position: absolute; top: 850px; left: 0; width: 100%; text-align: center;
    font-family: "Great Vibes", cursive; color: var(--gold); font-size: 56px;
  }
  .age-number { font-size: 96px; margin: 0 24px; vertical-align: -6px; }
  .origin {
    position: absolute; top: 995px; left: 0; width: 100%; text-align: center;
    font-family: "Josefin Sans", sans-serif; font-weight: 600; font-size: 20px;
    letter-spacing: 6px; color: var(--gold);
  }
  .specs {
    position: absolute; top: 1070px; left: 50%; transform: translateX(-50%);
    width: 560px; display: flex; justify-content: space-between;
    font-family: "Josefin Sans", sans-serif; font-weight: 600; color: var(--gold);
  }
  .spec-value { font-size: 34px; }
  .spec-unit { font-size: 22px; margin-left: 6px; }
</style>
</head>
<body>
<main class="label">
  <svg class="illustration" viewBox="0 0 440 470" role="img" aria-label="Illustration of a mulberry branch with green leaves and dark ripe berries">
    <defs>
      <radialGradient id="leafTone" cx="50%" cy="45%" r="55%">
        <stop offset="0%" stop-color="#8cc63f"/>
        <stop offset="60%" stop-color="#5e9b28" stop-opacity="0.7"/>
        <stop offset="100%" stop-color="#ffffff" stop-opacity="0"/>
      </radialGradient>
      <radialGradient id="berryTone" cx="50%" cy="50%" r="50%">
        <stop offset="0%" stop-color="#5a2e5e"/>
        <stop offset="100%" stop-color="#5a2e5e" stop-opacity="0"/>
      </radialGradient>
    </defs>
    <rect width="440" height="470" fill="url(#leafTone)"/>
    <ellipse cx="245" cy="290" rx="90" ry="120" fill="url(#berryTone)"/>
  </svg>

  <h1 class="brand">KOLVAT</h1>

  <div class="product">
    <div class="product-fruit">Mullberry</div>
    <div class="product-type">BRANDY</div>
  </div>

  <p class="age">Aged<span class="age-number">5</span>years</p>

  <p class="origin">MADE IN ARMENIA</p>

  <div class="specs">
    <p><span class="spec-value">51%</span><span class="spec-unit">ALC/VOL</span></p>
    <p><span class="spec-value">750</span><span class="spec-unit">ML</span></p>
  </div>
</main>
</body>
</html>
```